New Digital Marketing Company Needs Web Design

Introduction

Brightcrest gives advice to small businesses about their websites and digital marketing strategies and builds working relationships with clients to understand their business and maximise its online presence.

Brightcrest offers services to support its clients needs such as: website auditing & search engine optimisation (SEO), Quorvo Promoline, Chatterlane advertising, newsletter development & management, online performance reporting, email setup & management, website hosting, maintenance & backup, web development, web updates & web design.

Design Specification

The site should have a clean & professional look and use the colour scheme from the logo (attached below).

The design should consist of 2 templates; The homepage & content page.

Homepage Design

The homepage should have a header with logo, contact number and email and menu. Followed underneath by a slider and then individual blocks for key services. Under the key services should be a testimonial block with 3 testimonials. Finally the footer with company details, menu links and location map.

Header Info:

Contact number: 01632 960481
Email: info@brightcrest-demo.co.uk

Menu: Home Services About Contact

Slider Design:

The slider should be full page and show an image with text.

Key Services:

The key services should have a relevant icon and brief description.

The key services are:

Digital Marketing

Website Hosting & Management

Website Health Check (SEO)

Website Updating & Development

Newsletter Management

Email Management

Note: Lorem Ipsum can be used for brief description...

Testimonials:

There should be 3 testimonials side by side and they should include a headshot image of the person giving the testimonial.

Note: Lorem Ipsum and sample images can be used for testimonials...

Footer:

The footer should have 3 sections:

Menu links:

Digital Marketing About
Quorvo Promoline Contact
Chatterlane Advertising Privacy Policy
Search Engine Optimisation (SEO) Terms & Conditions
Website Hosting FAQ
Newsletter Management

Company Information:

BrightCrest
14 Marlow Close
Ashcombe
Berskhire
ZZ9 4QT
Tel: 01632 960481

Chatterlane icon - Pipwave icon - Careernest icon

Location

Quorvo map

Footer Bottom:

Copyright message.

Content Design

The content design should have the common header and footer.

Each content page should have a banner for image with text description (page title).

The content page should have area for text description and area for a video display if available.

There should be a right column (possibly) for modules (latest blog, latest Chatterlane feeds, testimonial)

Project Deadline Extended
Reason: I have had to extend the deadline as could not review while on vacation and need to feedback to some designers for content page design. Many thanks for your understanding.

Target Market(s)

Industry/Entity Type

Digital

Number of Pages Required

2 page

Requirements
Must have
• The site should have a clean & professional look and use the colour scheme from the logo (attached below).
• The design should consist of 2 templates; The homepage & content page.

```html
<!DOCTYPE html>
<html lang="en">
<head>
<meta charset="utf-8">
<title>BrightCrest – Digital Marketing</title>
<link rel="stylesheet" href="https://fonts.googleapis.com/css2?family=Lato:wght@700;900&family=Roboto:wght@400;500;700&display=swap">
<style>
:root{
  --plum:#66123f;
  --plum-dark:#5a0f38;
  --ink:#3b2a55;
  --text:#555;
  --muted:#8a8a8a;
  --light:#f3f3f3;
  --line:#c9c9c9;
  --white:#fff;
}
*{box-sizing:border-box;margin:0;padding:0}
html,body{width:1200px;height:2493px;overflow:hidden;background:var(--white)}
body{font-family:"Roboto",Arial,sans-serif;color:var(--text);position:relative}
.abs{position:absolute}

/* header */
.site-header{position:absolute;top:0;left:0;width:1200px;height:115px}
.brand{position:absolute;left:78px;top:24px;display:flex;align-items:center;gap:14px}
.brand-mark{width:56px;height:56px;border-radius:50%;background:var(--plum)}
.brand-name{font-size:44px;font-weight:700;color:var(--plum);letter-spacing:-.5px}
.call{position:absolute;left:893px;top:30px;display:flex;align-items:center;gap:12px}
.call-label{font-size:15px;color:var(--ink)}
.call-number{font-size:25px;font-weight:700;color:var(--plum);line-height:1.1}

/* nav */
.main-nav{position:absolute;top:115px;left:0;width:1200px;height:63px;background:var(--plum)}
.main-nav a{position:absolute;top:22px;font-size:18px;color:var(--white);text-decoration:none;opacity:.92}
.main-nav a.active{font-weight:500;opacity:1}
.search{position:absolute;right:44px;top:19px}

/* hero */
.hero{position:absolute;top:178px;left:0;width:1200px;height:497px;
  background:linear-gradient(90deg,#b7b4b2 0%,#d8cdbf 45%,#e9d6b8 70%,#c79a6f 100%)}
.hero-person{position:absolute;right:60px;top:50px;width:380px;height:447px;border-radius:180px 180px 0 0;
  background:linear-gradient(180deg,#6b4b3a 0%,#3a3036 60%,#2e2a30 100%);opacity:.55}
.hero-title{position:absolute;left:80px;top:148px;font-family:"Lato",Arial,sans-serif;font-weight:900;
  font-size:56px;line-height:68px;color:#111;text-transform:uppercase}
.hero-btn{position:absolute;left:78px;top:297px;width:269px;height:60px;border-radius:30px;background:var(--plum);
  color:var(--white);font-size:22px;display:flex;align-items:center;justify-content:center}
.hero-arrow{position:absolute;top:209px;width:50px;height:50px;border-radius:50%;border:2px solid #555;display:flex;align-items:center;justify-content:center}

/* welcome */
.section-title{position:absolute;left:0;width:1200px;text-align:center;font-size:41px;color:var(--plum);font-weight:400}
.section-lead{position:absolute;left:180px;width:840px;text-align:center;font-size:14.5px;line-height:27px;color:var(--muted)}
.service{position:absolute;width:340px;display:flex;gap:20px}
.service-icon{flex:none;width:95px;height:95px;border-radius:50%;background:#eee;border:1px solid #ddd;display:flex;align-items:center;justify-content:center}
.service-icon.featured{background:var(--plum);border-color:var(--plum)}
.service h3{font-size:20px;font-weight:400;color:var(--plum);line-height:25px;margin-top:8px}
.service.alt h3{color:var(--ink)}
.service p{font-size:15px;line-height:25px;color:#555;margin-top:2px}

/* testimonials */
.testimonials{position:absolute;top:1202px;left:0;width:1200px;height:302px;background:var(--light)}
.quote-mark{position:absolute;font-family:Georgia,serif;font-size:150px;color:#d9d9d9;line-height:1}
.testimonial-text{position:absolute;left:200px;top:128px;width:800px;text-align:center;font-size:14.5px;line-height:26px;color:#666}
.client{position:absolute;left:0;top:216px;width:1200px;text-align:center;font-size:15px;color:var(--ink)}
.client b{font-weight:700}

/* contact */
.field{position:absolute;border:1.5px solid var(--line);border-radius:3px;background:var(--white);font-size:14.5px;color:#444;padding:10px 12px}
.submit{position:absolute;left:512px;top:1886px;width:174px;height:55px;border-radius:28px;background:var(--plum);color:var(--white);
  font-size:21px;font-weight:500;display:flex;align-items:center;justify-content:center}

/* map */
.map{position:absolute;top:2004px;left:0;width:1200px;height:167px;
  background:linear-gradient(100deg,#cfe0c2 0%,#9fc1de 22%,#e4e6d8 35%,#ece9df 70%,#e4e3d6 100%)}

/* footer */
.site-footer{position:absolute;top:2171px;left:0;width:1200px;height:322px;background:var(--plum-dark);color:var(--white)}
.footer-col{position:absolute;top:38px}
.footer-col h4{font-size:15px;font-weight:700;letter-spacing:.2px;margin-bottom:18px}
.links li{list-style:none;font-size:13.5px;line-height:28px;color:#eadbe3}
.links li::before{content:"» ";}
.info-row{display:flex;gap:12px;font-size:13.5px;line-height:22px;color:#eadbe3;margin-bottom:18px}
.info-row strong{color:var(--white);font-weight:500}
.social{display:flex;align-items:center;gap:16px;margin-bottom:10px;font-size:15px}
.social-dot{width:45px;height:45px;border-radius:50%;background:#e9e3e6}
.footer-rule{position:absolute;left:78px;top:258px;width:1044px;height:1px;background:rgba(255,255,255,.25)}
.copyright{position:absolute;left:0;top:282px;width:1200px;text-align:center;font-size:14px;color:#eadbe3}
.copyright b{color:var(--white)}
</style>
</head>
<body>

<header class="site-header">
  <div class="brand">
    <span class="brand-mark"></span>
    <span class="brand-name">BrightCrest</span>
  </div>
  <div class="call">
    <svg width="50" height="50" viewBox="0 0 24 24"><path fill="#66123f" d="M6.6 10.8a15.1 15.1 0 0 0 6.6 6.6l2.2-2.2a1 1 0 0 1 1-.25 11.4 11.4 0 0 0 3.6.57 1 1 0 0 1 1 1V20a1 1 0 0 1-1 1A17 17 0 0 1 3 4a1 1 0 0 1 1-1h3.5a1 1 0 0 1 1 1c0 1.25.2 2.45.57 3.57a1 1 0 0 1-.25 1z"/></svg>
    <div>
      <div class="call-label">Call Us Now</div>
      <div class="call-number">01632 960481</div>
    </div>
  </div>
</header>

<nav class="main-nav">
  <a class="active" style="left:108px">HOME</a>
  <a style="left:226px">ABOUT US</a>
  <a style="left:384px">SERVICES</a>
  <a style="left:537px">CONTACT US</a>
  <svg class="search" width="26" height="26" viewBox="0 0 24 24"><circle cx="10" cy="10" r="6.5" fill="none" stroke="#fff" stroke-width="2.6"/><path d="M15 15l6 6" stroke="#fff" stroke-width="2.8" stroke-linecap="round"/></svg>
</nav>

<section class="hero" role="img" aria-label="Slider photo: smiling woman in glasses holding a tablet in front of a blurred glass office building">
  <div class="hero-person"></div>
  <h1 class="hero-title">Lorem ipsum is simple<br>dummy text</h1>
  <div class="hero-btn">CONTACT KNOW US</div>
  <div class="hero-arrow" style="left:13px"><svg width="18" height="18" viewBox="0 0 24 24"><path d="M15 4l-8 8 8 8" fill="none" stroke="#444" stroke-width="2"/></svg></div>
  <div class="hero-arrow" style="left:1136px"><svg width="18" height="18" viewBox="0 0 24 24"><path d="M9 4l8 8-8 8" fill="none" stroke="#444" stroke-width="2"/></svg></div>
</section>

<h2 class="section-title" style="top:733px">WELCOME TO BRIGHTCREST</h2>
<p class="section-lead" style="top:794px">Lorem Ipsum is simply dummy text of the printing and typesetting industry. Lorem Ipsum has been the industry's standard dummy text ever since the when an unknown printer took a galley</p>

<div class="service" style="left:78px;top:891px">
  <div class="service-icon featured"><svg width="46" height="46" viewBox="0 0 24 24"><circle cx="10" cy="13" r="6" fill="#fff"/><path d="M14 4a6 6 0 0 1 6 6M14 7a3 3 0 0 1 3 3" fill="none" stroke="#fff" stroke-width="1.6"/></svg></div>
  <div><h3>Digital<br>Marketing</h3><p>Lorem Ipsum is simply dummy text of the printing and.</p></div>
</div>
<div class="service alt" style="left:430px;top:891px">
  <div class="service-icon"><svg width="46" height="46" viewBox="0 0 24 24"><rect x="4" y="4" width="16" height="4" fill="#3b2a55"/><rect x="4" y="10" width="16" height="4" fill="#3b2a55"/><rect x="4" y="16" width="16" height="4" fill="#3b2a55"/></svg></div>
  <div><h3>Website Hosting &amp;<br>Management</h3><p>Lorem Ipsum is simply dummy text of the printing and.</p></div>
</div>
<div class="service alt" style="left:786px;top:891px">
  <div class="service-icon"><svg width="46" height="46" viewBox="0 0 24 24"><rect x="3" y="5" width="17" height="13" fill="none" stroke="#3b2a55" stroke-width="1.6"/><path d="M9 10l-2 2 2 2M14 10l2 2-2 2" fill="none" stroke="#3b2a55" stroke-width="1.4"/></svg></div>
  <div><h3>Website Updating &amp;<br>Development</h3><p>Lorem Ipsum is simply dummy text of the printing and.</p></div>
</div>
<div class="service alt" style="left:78px;top:1037px">
  <div class="service-icon"><svg width="46" height="46" viewBox="0 0 24 24"><circle cx="12" cy="8" r="4" fill="#3b2a55"/><path d="M4 21c0-5 3.5-8 8-8s8 3 8 8z" fill="#3b2a55"/></svg></div>
  <div><h3>Website Health Check<br>(SEO)</h3><p>Lorem Ipsum is simply dummy text of the printing and.</p></div>
</div>
<div class="service alt" style="left:430px;top:1037px">
  <div class="service-icon"><svg width="46" height="46" viewBox="0 0 24 24"><rect x="3" y="6" width="18" height="12" fill="#3b2a55"/><path d="M3 6l9 7 9-7" fill="none" stroke="#fff" stroke-width="1.3"/></svg></div>
  <div><h3>Email<br>Management</h3><p>Lorem Ipsum is simply dummy text of the printing and.</p></div>
</div>
<div class="service alt" style="left:786px;top:1037px">
  <div class="service-icon"><svg width="46" height="46" viewBox="0 0 24 24"><rect x="5" y="4" width="13" height="16" transform="rotate(40 12 12)" fill="none" stroke="#3b2a55" stroke-width="1.6"/><path d="M9 10h6M9 13h6" stroke="#3b2a55" stroke-width="1.3" transform="rotate(40 12 12)"/></svg></div>
  <div><h3>Newsletter<br>Management</h3><p>Lorem Ipsum is simply dummy text of the printing and.</p></div>
</div>

<section class="testimonials">
  <h2 class="section-title" style="top:63px">TESTIMONIALS</h2>
  <div class="quote-mark" style="left:135px;top:70px">“</div>
  <p class="testimonial-text">" Lorem Ipsum is simply dummy text of the printing and typesetting industry. Lorem Ipsum has been the industry's standard dummy text ever since the 1500s, when an unknown printer took a galley of type and scrambled it to make a type specimen book. It has survived "</p>
  <div class="client"><b>CLIENT NAME</b> - sampleclient.test</div>
  <div class="quote-mark" style="left:996px;top:172px">”</div>
</section>

<h2 class="section-title" style="top:1562px">CONTACT US</h2>
<p class="section-lead" style="top:1620px;left:250px;width:700px;line-height:24px;color:#666">" Lorem Ipsum is simply dummy text of the printing and typesetting industry been the industry's s simply dummy text of the printing and typesetting indust</p>
<div class="field" style="left:241px;top:1682px;width:352px;height:40px">Name*</div>
<div class="field" style="left:605px;top:1682px;width:354px;height:40px">Email*</div>
<div class="field" style="left:241px;top:1732px;width:352px;height:41px">Phone*</div>
<div class="field" style="left:605px;top:1732px;width:354px;height:41px">Services*
  <svg class="abs" style="right:12px;top:16px" width="16" height="9" viewBox="0 0 16 9"><path d="M0 0h16L8 9z" fill="#555"/></svg></div>
<div class="field" style="left:241px;top:1783px;width:718px;height:92px">Message*</div>
<div class="submit">SUBMIT</div>

<div class="map" role="img" aria-label="Location map showing the office area, river and surrounding roads"></div>

<footer class="site-footer">
  <div class="footer-col" style="left:80px">
    <h4>USEFUL LINKS</h4>
    <ul class="links">
      <li>Digital Marketing About</li>
      <li>Quorvo Promoline Contact</li>
      <li>Chatterlane Advertising Privacy Policy</li>
      <li>(SEO) Terms &amp; Conditions</li>
      <li>Website Hosting FAQ</li>
      <li>Newsletter Management</li>
    </ul>
  </div>
  <div class="footer-col" style="left:457px">
    <h4>COMPANY INFORMATION</h4>
    <div class="info-row">
      <svg width="20" height="24" viewBox="0 0 20 24"><path d="M10 23s8-8 8-14a8 8 0 0 0-16 0c0 6 8 14 8 14z" fill="none" stroke="#fff" stroke-width="1.5"/><circle cx="10" cy="9" r="3" fill="none" stroke="#fff" stroke-width="1.5"/></svg>
      <div><strong>BRIGHTCREST</strong><br>BrightCrest 14 Marlow Close Ashcombe<br>Westshire ZZ9 4QT</div>
    </div>
    <div class="info-row">
      <svg width="20" height="20" viewBox="0 0 24 24"><path d="M6.6 10.8a15.1 15.1 0 0 0 6.6 6.6l2.2-2.2a1 1 0 0 1 1-.25 11.4 11.4 0 0 0 3.6.57 1 1 0 0 1 1 1V20a1 1 0 0 1-1 1A17 17 0 0 1 3 4a1 1 0 0 1 1-1h3.5a1 1 0 0 1 1 1c0 1.25.2 2.45.57 3.57a1 1 0 0 1-.25 1z" fill="none" stroke="#fff" stroke-width="1.5"/></svg>
      <div>01632 960481</div>
    </div>
    <div class="info-row">
      <svg width="20" height="20" viewBox="0 0 24 24"><rect x="2" y="5" width="20" height="14" fill="none" stroke="#fff" stroke-width="1.6"/><path d="M2 5l10 8 10-8" fill="none" stroke="#fff" stroke-width="1.6"/></svg>
      <div>info@brightcrest-demo.co.uk</div>
    </div>
  </div>
  <div class="footer-col" style="left:813px">
    <h4>FOLLOW US ON</h4>
    <div class="social"><span class="social-dot"></span>Chatterlane</div>
    <div class="social"><span class="social-dot"></span>Pipwave</div>
    <div class="social"><span class="social-dot"></span>Careernest</div>
  </div>
  <div class="footer-rule"></div>
  <p class="copyright">©<b>BrightCrest</b>- 2016. All Rights Reserved</p>
</footer>

</body>
</html>
```